Geschäftspapiere für Unternehmensberatung
Zielgruppe
Unternehmensberatung,
Vorstände, Geschäftsführer, Personalleiter, Führungskräfte
Aufgabenstellung
Das Briefpapier muss veränderbar sein, da die Daten sich noch ändern werden. Diese liegen aber erst nach der Ummeldung im Handelsregister endgültig vor.
Eine Vorlage unseres alten Briefpapiers folgt.

```html
<!DOCTYPE html>
<html lang="de">
<head>
<meta charset="utf-8">
<title>Briefbogen – Nordlicht Beratungshaus</title>
<link rel="stylesheet" href="https://fonts.googleapis.com/css2?family=Arimo:wght@400&family=Open+Sans:wght@400;600&display=swap">
<style>
  :root {
    --backdrop: #e6e6e6;
    --paper: #ffffff;
    --ink: #111111;
    --accent: #3a4fa8;
  }
  * { margin: 0; padding: 0; box-sizing: border-box; }
  html, body { width: 1200px; height: 1200px; overflow: hidden; background: var(--backdrop); }
  .letter {
    position: absolute; left: 212px; top: 52px; width: 776px; height: 1096px;
    background: var(--paper); color: var(--ink);
    font-family: "Arimo", Arial, sans-serif;
  }
  .abs { position: absolute; }
  .brand {
    left: 420px; top: 62px; display: flex; align-items: center; gap: 12px;
    font-family: "Open Sans", sans-serif; font-weight: 600; font-size: 22px;
    line-height: 1.15; color: var(--ink); letter-spacing: 0.5px;
  }
  .brand-dot { width: 14px; height: 14px; border-radius: 50%; background: var(--accent); flex: none; }
  .sender-line { left: 92px; top: 190px; font-family: "Open Sans", sans-serif; font-size: 7.6px; white-space: nowrap; }
  .recipient { left: 92px; top: 209px; font-size: 14px; line-height: 18.6px; }
  .recipient .city { margin-top: 18px; }
  .side-info {
    left: 564px; top: 189px; height: 129px; border-left: 1px solid var(--accent);
    padding-left: 17px; font-family: "Open Sans", sans-serif; font-size: 9.5px; line-height: 14.4px;
  }
  .contact { margin-top: 12px; list-style: none; }
  .contact li { display: flex; align-items: center; gap: 5px; }
  .contact svg { width: 9px; height: 9px; flex: none; }
  .fold-mark { left: 0; width: 37px; height: 1px; background: var(--accent); }
  .subject { left: 92px; top: 394px; font-size: 14px; }
  .body-text { left: 92px; top: 433px; width: 640px; font-size: 14px; line-height: 19.6px; }
  .body-text p + p { margin-top: 19.6px; }
  .closing { left: 92px; top: 805px; font-size: 14px; }
  .footer-col {
    top: 1013px; height: 58px; border-left: 1px solid var(--accent); padding-left: 17px;
    font-family: "Open Sans", sans-serif; font-size: 9.5px; line-height: 14.4px; white-space: nowrap;
  }
</style>
</head>
<body>
<main class="letter">
  <div class="abs brand"><span class="brand-dot"></span><span>NORDLICHT<br>BERATUNGSHAUS</span></div>

  <p class="abs sender-line">Nordlicht Beratungshaus GmbH | Am Weidenhang 7 | 21465 Reinbek</p>

  <address class="abs recipient" style="font-style:normal">
    Herrn<br>Max Mustermann<br>Musterstraße 00
    <div class="city">01234 Musterstadt</div>
  </address>

  <aside class="abs side-info">
    Nordlicht<br>Beratungshaus GmbH<br>Am Weidenhang 7<br>21465 Reinbek
    <ul class="contact">
      <li><svg viewBox="0 0 10 10"><path d="M2 1l2 2-1 1.2a6 6 0 0 0 2.8 2.8L7 6l2 2-1.2 1.2C4.5 9 1 5.5.8 2.2Z" fill="none" stroke="var(--accent)" stroke-width="1"/></svg>040 5512340</li>
      <li><svg viewBox="0 0 10 10"><rect x="1" y="4" width="8" height="4" rx="1" fill="var(--accent)"/><rect x="2.5" y="1" width="5" height="3" fill="none" stroke="var(--accent)"/></svg>040 5512346</li>
      <li><svg viewBox="0 0 10 10"><rect x="1" y="2.5" width="8" height="5.5" fill="none" stroke="var(--accent)"/><path d="M1 2.5l4 3 4-3" fill="none" stroke="var(--accent)"/></svg>kontakt@nordlicht-beratung.de</li>
      <li><svg viewBox="0 0 10 10"><circle cx="5" cy="5" r="4" fill="none" stroke="var(--accent)"/><path d="M1 5h8M5 1c-2 2.5-2 5.5 0 8M5 1c2 2.5 2 5.5 0 8" fill="none" stroke="var(--accent)" stroke-width=".7"/></svg>www.nordlicht-beratung.de</li>
    </ul>
  </aside>

  <span class="abs fold-mark" style="top:388px"></span>
  <span class="abs fold-mark" style="top:548px"></span>
  <span class="abs fold-mark" style="top:775px"></span>

  <h1 class="abs subject" style="font-weight:400">Dies ist eine Betreffzeile</h1>

  <div class="abs body-text">
    <p>Sehr geehrter Herr Mustermann, jeder Setzer hat für diesen Zweck immer etwas Blindtext parat. Blindtext ist im Umfang von einigen tausend Anschlägen, der für die »äußerliche« Gestaltung einer Publikation verwendet und dessen Inhalt unwichtig ist. Man setzt ihn oft zum Beispiel in verschiedenen Schriften und Schriftgrößen, um anderen zu zeigen, wie eine bestimmte Schrift wirkt.</p>
    <p>Oder man montiert auch komplette ganze Seiten mit sinnlosen Streifen von Blindtext, um das spätere Aussehen der Seiten zu simulieren. Blindtext wird allerdings oft nur für die Teile einer Seite verwendet, die in so kleiner Schrift gesetzt werden, dass sie beim »Überfliegen« ungelesen bleiben.</p>
    <p>Jeder Setzer hat für diesen Zweck immer etwas Blindtext parat. Blindtext ist Umfang von einigen tausend Anschlägen, der für die »äußerliche« Gestaltung einer Publikation verwendet und dessen Inhalt unwichtig ist.</p>
  </div>

  <p class="abs closing">Mit freundlichen Grüßen</p>

  <footer>
    <div class="abs footer-col" style="left:92px">Geschäftsführer:<br>Lennart Holmberg<br>Kristina Albers<br>Marlene Ohlsen Holmberg</div>
    <div class="abs footer-col" style="left:318px">Kiel, HRB 4592 KI<br>Steuernummer: 31 418 62093<br>USt-IdNr.: DE 927364105</div>
    <div class="abs footer-col" style="left:564px">Hansebank Hamburg<br>IBAN: DE45 2005 0000 0713 2289 40<br>BIC: HSBKDEHHXXX</div>
  </footer>
</main>
</body>
</html>
```